Business Card Design for Pastor/Church Leadership - simple, elegant, "different"

Design a name card based on logo and color from our branding guide - see file "BWF Logo and Color".
The teal frame around the logo is not part of the logo and is a not necessary design element for the name card (as the attached PDF file may suggest).
The font suggested by branding is "Frutiger 55 Roman".
The file "not good.pdf", a sample of a name card that is NOT good.
- fonts too small to read
- the tagline on the logo "Still waters, bright path" not easy to read with logo used in this design
- "MAPLE GROVE CHAPEL" unnecessarily duplicated - possibly because logo too small
- not sure about the green frame, probably better to drop

Target Market(s)

broad, all people the pastor of an international church in Tokyo meets

Industry/Entity Type

Business

Contact Information for Business Card

Everett L. Pranzoni
Pastor
3-9-4 Kamiyacho, Shibuya-ku
Tokyo 150-0082 (Church)
2-18 Sarugakucho, Shibuya-ku
Tokyo 150-0046 (Home)
Tel: 03-5712-0368
E-mail: pastor@maplegrovechapel.org
URL: http://www.maplegrovechapel.org

Font styles to use
Sans Serif
Other font styles liked:
• Frutiger 55 Roman (want, not must)

Requirements
Must have
• must include logo
• must make use of the "bright turquoise color"
• Cyan = 59, Magenta = 0, Yellow=24, Black=0
• Red=3.1%, Green=91%, Blue=87.1%
• Key Info (name) must be easy to read (see notes on bad sample namecard attached)

```html
<!DOCTYPE html>
<html lang="en">
<head>
<meta charset="utf-8">
<title>Maple Grove Chapel – Business Card</title>
<link rel="stylesheet" href="https://fonts.googleapis.com/css2?family=Noto+Sans:wght@400&family=Arimo:wght@400&display=swap">
<style>
  :root {
    --teal: #5bc8c8;
    --ink: #555555;
    --card: #ffffff;
    --backdrop: #444444;
  }
  * { margin: 0; padding: 0; box-sizing: border-box; }
  html, body {
    width: 900px; height: 1200px; overflow: hidden;
    background: var(--backdrop);
    font-family: "Noto Sans", sans-serif;
  }
  .canvas { position: relative; width: 900px; height: 1200px; }
  .card {
    position: absolute; left: 108px; width: 679px; height: 397px;
    background: var(--card); overflow: hidden;
  }
  .card--front { top: 166px; }
  .card--back { top: 635px; }

  /* Front */
  .front-mark {
    position: absolute; left: 318px; top: 150px;
    width: 44px; height: 44px; background: var(--teal);
  }
  .front-name {
    position: absolute; left: 145px; top: 250px; width: 389px;
    text-align: center; color: var(--teal);
    font-size: 28px; letter-spacing: 2px; line-height: 36px; white-space: nowrap;
  }
  .front-rule {
    position: absolute; left: 145px; top: 291px; width: 389px; height: 2px;
    background: var(--teal);
  }
  .front-tagline {
    position: absolute; left: 145px; top: 297px; width: 389px;
    text-align: center; color: var(--teal);
    font-size: 18px; letter-spacing: 1px; line-height: 26px;
  }

  /* Back */
  .back-mark {
    position: absolute; left: 191px; top: 20px;
    width: 73px; height: 73px; background: var(--teal);
  }
  .back-name {
    position: absolute; left: 308px; top: 44px; width: 306px;
    color: var(--teal); font-size: 23px; line-height: 32px; white-space: nowrap;
  }
  .back-rule {
    position: absolute; left: 308px; top: 77px; width: 306px; height: 2px;
    background: var(--teal);
  }
  .back-tagline {
    position: absolute; left: 308px; top: 83px; width: 306px;
    text-align: center; color: var(--teal);
    font-family: "Arimo", sans-serif; font-size: 20px; line-height: 28px;
  }
  .person { position: absolute; left: 308px; top: 134px; }
  .person-name { color: var(--ink); font-size: 21px; line-height: 30px; }
  .person-role { color: var(--teal); font-size: 16px; line-height: 20px; }
  .addresses {
    position: absolute; left: 308px; top: 198px;
    color: var(--ink); font-size: 14.5px; line-height: 21.5px;
  }
  .contacts {
    position: absolute; left: 308px; top: 298px; list-style: none;
    color: var(--ink); font-size: 14.5px; line-height: 21.5px;
  }
  .contacts li { display: flex; align-items: center; gap: 9px; }
  .contacts svg { width: 13px; height: 13px; fill: var(--teal); flex: none; }
</style>
</head>
<body>
<main class="canvas">
  <section class="card card--front">
    <div class="front-mark"></div>
    <div class="front-name">MAPLE GROVE CHAPEL</div>
    <div class="front-rule"></div>
    <div class="front-tagline">Still waters, bright path</div>
  </section>

  <section class="card card--back">
    <div class="back-mark"></div>
    <div class="back-name">MAPLE GROVE CHAPEL</div>
    <div class="back-rule"></div>
    <div class="back-tagline">Still waters, bright path</div>

    <div class="person">
      <p class="person-name">Everett L. Pranzoni</p>
      <p class="person-role">Pastor</p>
    </div>

    <div class="addresses">
      <p>3-9-4 Kamiyacho, Shibuya-ku</p>
      <p>Tokyo 150-0082 (Church)</p>
      <p>2-18 Sarugakucho, Shibuya-ku</p>
      <p>Tokyo 150-0046 (Home)</p>
    </div>

    <ul class="contacts">
      <li>
        <svg viewBox="0 0 16 16" aria-hidden="true"><path d="M3.5 1l2.5 3-1.5 2c1 2 3 4 5 5l2-1.5 3 2.5-1.5 2.5C7 15 1 9 1 2.5z"/></svg>
        <span>03-5712-0368</span>
      </li>
      <li>
        <svg viewBox="0 0 16 16" aria-hidden="true"><path d="M1 3h14v10H1z M2 4.2v.6l6 4 6-4v-.6l-6 4z" fill-rule="evenodd"/></svg>
        <span>pastor@maplegrovechapel.org</span>
      </li>
      <li>
        <svg viewBox="0 0 16 16" aria-hidden="true"><path fill="none" stroke="#5bc8c8" stroke-width="1.3" d="M8 1.5a6.5 6.5 0 1 0 .01 0zM1.5 8h13M8 1.5c-3 3.5-3 9.5 0 13M8 1.5c3 3.5 3 9.5 0 13M2.5 4.8h11M2.5 11.2h11"/></svg>
        <span>www.maplegrovechapel.org</span>
      </li>
    </ul>
  </section>
</main>
</body>
</html>
```